Web Design Project For Hot Tub Company [DETAILED instructions inside with a VIDEO!!]

Site will be aimed at individual consumers and not business owners. The purpose of the site is NOT to sell hot tubs online, but to entice people to come to the actual store.

According to the client, it is mostly MEN who initiate contact, while the WOMEN come into the store. This means, the design elements should appeal to MEN more so than to WOMEN.

Right now, the clients only web presence is this Brindle Listings ad:

-LINK-
http://www.brindlelistings.example/albuquerque-nm/mip/spa-shop-albuquerque-813274605
-

Site layout will include an area for a large video on the top, below the menu bar. There will be NO optin form on this site, so there will be some open space next to the video. Be creative and use it to highlight something unique about the business (they pride themselves on their high-end products, low monthly maintenance fees, and after purchase care-the company offers FREE delivery, installation, training, 2 free "drain and fills" and a 30-exchange guarantee.) with an interesting graphic.

Below that, a standard FOUR column layout with images and text that can be hyperlinked later to interior pages. Interior pages will include a sidebar. Below that, a standard footer.

Navigation will include the following: Home, About Us, Models, After Market Service, Testimonials, , and Contact Us.

Ideally, this company's site should appeal to higher income couples without children, new homeowners, and wealthy families.

Company's Logo is attached

Target Market(s)

Upper middle class to upper class families-boyfriends, husbands and fathers mostly.

Industry/Entity Type

Business

Requirements
Must have
• -Area for a video player
-Fun, inviting layout that will appeal to upper middle class husbands and boyfriends.
Nice to have
• *Creativity!!!!

A website with a header, a horizontal navigation bar, a video, a four column layout, and a footer are pretty common and standard. Use your creativity to stay within our parameters without looking like a boring, cookie-cutter website.

Though the site should appeal to men, do not exclude women.
Should not have
• *An optin form

```html
<!DOCTYPE html>
<html lang="en">
<head>
<meta charset="utf-8">
<title>Spa Shop Albuquerque</title>
<link href="https://fonts.googleapis.com/css2?family=Questrial&family=Exo:wght@400;700;800&family=Titillium+Web:wght@300;400&display=swap" rel="stylesheet">
<style>
:root{
  --blue:#12aee8;
  --blue-dark:#0a8fc4;
  --ink:#2b2b2b;
  --text:#666;
  --muted:#8a8a8a;
  --line:#c9c9c9;
  --tile:#ececec;
  --footer:#efefef;
  --white:#fff;
}
*{margin:0;padding:0;box-sizing:border-box}
html,body{width:1200px;height:1200px;overflow:hidden;background:var(--white)}
body{position:relative;font-family:"Titillium Web",sans-serif;color:var(--text)}
.abs{position:absolute}

.site-header{left:0;top:0;width:1200px;height:81px;background:linear-gradient(#fff 0,#fff 50%,#f3f3f3 100%);border-top:2px solid #e4e4e4;border-bottom:2px solid #d8d8d8}
.brand{left:171px;top:26px;display:flex;align-items:center;gap:8px;font-family:"Exo",sans-serif;font-weight:700;font-size:16px;color:var(--blue)}
.brand-dot{width:22px;height:22px;border-radius:50%;background:var(--blue)}
.main-nav{left:385px;top:0;height:81px;display:flex;align-items:center;font-family:"Questrial",sans-serif;font-size:12.5px;color:var(--ink);letter-spacing:-.4px;white-space:nowrap}
.main-nav a{color:inherit;text-decoration:none;padding:0 9px;border-left:1px dotted #aaa;line-height:12px}
.main-nav a.home{border:none;background:var(--blue);color:#fff;height:81px;line-height:84px;width:61px;text-align:center;padding:0;margin-right:12px}
.social{left:954px;top:31px;display:flex;gap:3px}
.social span{width:22px;height:22px;border-radius:50%;background:var(--blue)}

.hero{left:0;top:81px;width:1200px;height:329px;background:radial-gradient(ellipse at 50% 45%,#3d4f5e 0,#262a30 40%,#121212 80%)}
.play{left:557px;top:201px}
.hero-shadow{left:171px;top:410px;width:857px;height:22px;background:radial-gradient(ellipse at 50% 0,rgba(0,0,0,.18),rgba(0,0,0,0) 70%)}

.section-title{left:171px;width:857px;border-bottom:1px dotted var(--line);padding:0 2px 4px}
.welcome{top:444px;font-family:"Questrial",sans-serif;font-weight:400;font-size:21px;color:var(--ink);letter-spacing:-.5px}
.welcome strong{font-family:"Exo",sans-serif;font-weight:800;color:var(--blue);letter-spacing:-.3px}
.intro{left:173px;top:482px;width:790px;font-size:11px;line-height:14.3px;font-weight:300;color:#555}
.btn{background:var(--blue);color:#fff;font-family:"Exo",sans-serif;font-size:11px;text-decoration:none;display:block;text-align:center}
.read-more{left:171px;top:546px;width:70px;height:25px;line-height:25px}

.heading{font-family:"Exo",sans-serif;font-weight:800;font-size:17px;color:#333}
.services-title{top:612px}
.services{left:171px;top:657px;width:857px;height:112px}
.service{position:absolute;top:0;width:112px;height:112px}
.service svg.tile{position:absolute;left:0;top:0}
.service .icon{position:absolute;left:36px;top:14px}
.service .label{position:absolute;left:0;width:112px;text-align:center;font-family:"Exo",sans-serif;font-weight:700;font-size:11px;line-height:12px;color:#444}

.products-title{top:791px}
.product{position:absolute;top:830px;width:208px}
.product .photo{width:208px;height:105px}
.product p{margin-top:16px;font-family:"Questrial",sans-serif;font-size:9.5px;line-height:13px;color:#333;text-transform:uppercase;white-space:nowrap}
.product .btn{margin-top:8px;width:73px;height:26px;line-height:26px;font-size:12px}

.site-footer{left:0;top:1055px;width:1200px;height:145px;background:var(--footer)}
.foot-col{top:1073px}
.foot-col h3{font-family:"Questrial",sans-serif;font-weight:400;font-size:14px;color:#555;border-bottom:1px dotted var(--line);padding-bottom:3px;width:145px;margin-bottom:8px}
.foot-col p,.foot-col li{font-family:"Questrial",sans-serif;font-size:9px;line-height:13px;color:var(--muted);text-transform:uppercase;list-style:none;white-space:nowrap}
.accessories li{border-bottom:1px dotted var(--line);padding:4px 0 5px;width:145px;letter-spacing:-.1px}
.newsletter-form{left:171px;top:1133px;display:flex}
.newsletter-form .field{width:174px;height:28px;background:#fff;border:1px solid #ddd}
.newsletter-form .send{height:28px;line-height:28px;padding:0 16px 0 6px;font-size:12px;clip-path:polygon(0 0,88% 0,100% 50%,88% 100%,0 100%)}
.contact p{line-height:14.5px}
.copyright{left:0;top:1173px;width:1200px;border-top:1px dotted var(--line);text-align:center;font-family:"Questrial",sans-serif;font-size:10px;color:#999;padding-top:5px}
</style>
</head>
<body>

<header class="site-header abs"></header>
<div class="brand abs"><span class="brand-dot"></span>Spa Shop Albuquerque</div>
<nav class="main-nav abs">
  <a class="home" href="#">HOME</a>
  <a href="#">ABOUT US</a>
  <a href="#">MODELS</a>
  <a href="#">MARKET SERVICES</a>
  <a href="#">TESTIMONIALS</a>
  <a href="#" style="border-right:1px dotted #aaa">CONTACT US</a>
</nav>
<div class="social abs"><span></span><span></span><span></span></div>

<div class="hero abs" role="img" aria-label="Video still of a round hot tub on a terrace overlooking the sea at dusk"></div>
<svg class="play abs" width="86" height="86" viewBox="0 0 86 86" aria-label="Play video">
  <circle cx="43" cy="43" r="38" fill="none" stroke="#fff" stroke-width="7"/>
  <path d="M36 29 L58 43 L36 57 Z" fill="#fff"/>
</svg>
<div class="hero-shadow abs"></div>

<h1 class="section-title welcome abs">WELLCOME TO <strong>SPA SHOP ALBUQUERQUE</strong></h1>
<p class="intro abs">Lorem ipsum dolor sit amet, consectetuer adipiscing elit, sed diam nonummy nibh euismod tincidunt ut laoreet dolore magna aliquam erat volutpat. Ut wisi enim ad minim veniam, quis nostrud exerci tation ullamcorper suscipit lobortis nisl ut aliquip ex ea commodo consequat. Duis autem vel eum iriure dolor in hendrerit in vulputate velit esse molestie consequat, vel illum dolore eu feugiat nulla facilisis at vero eros et accumsan et iusto odio dignissim qui blandit praesent luptatum zzril delenit augue duis dolore te feugait nulla facilisi.</p>
<a class="btn read-more abs" href="#">READ MORE</a>

<h2 class="section-title heading services-title abs">OUR SERVICES</h2>
<div class="services abs">
  <div class="service" style="left:0">
    <svg class="tile" width="112" height="112"><polygon points="33,0 79,0 112,33 112,79 79,112 33,112 0,79 0,33" fill="var(--tile)"/></svg>
    <svg class="icon" width="40" height="40" viewBox="0 0 40 40"><path d="M20 2 L25 15 L39 15 L28 24 L32 38 L20 29 L8 38 L12 24 L1 15 L15 15 Z" fill="var(--blue)"/></svg>
    <div class="label" style="top:74px">HIGH-END<br>PRODUCTS</div>
  </div>
  <div class="service" style="left:124px">
    <svg class="tile" width="112" height="112"><polygon points="33,0 79,0 112,33 112,79 79,112 33,112 0,79 0,33" fill="var(--tile)"/></svg>
    <svg class="icon" width="40" height="40" viewBox="0 0 40 40"><path d="M24 3 L37 3 L37 16 L17 36 L4 23 Z" fill="var(--blue)"/><circle cx="31" cy="9" r="2.5" fill="var(--tile)"/><text x="19" y="25" font-family="Exo,sans-serif" font-weight="800" font-size="13" fill="#fff" text-anchor="middle" transform="rotate(-45 19 21)">$</text></svg>
    <div class="label" style="top:68px">LOW<br>MAINTINANCE<br>FEES</div>
  </div>
  <div class="service" style="left:250px">
    <svg class="tile" width="112" height="112"><polygon points="33,0 79,0 112,33 112,79 79,112 33,112 0,79 0,33" fill="var(--tile)"/></svg>
    <svg class="icon" width="40" height="40" viewBox="0 0 40 40"><path d="M2 18 Q20 -4 38 18 Z" fill="var(--blue)"/><path d="M20 18 L20 33 Q20 38 15 38 Q11 38 11 33" fill="none" stroke="var(--blue)" stroke-width="3"/></svg>
    <div class="label" style="top:70px">AFTER<br>PURCHASE<br>CARE</div>
  </div>
  <div class="service" style="left:374px">
    <svg class="tile" width="112" height="112"><polygon points="33,0 79,0 112,33 112,79 79,112 33,112 0,79 0,33" fill="var(--tile)"/></svg>
    <svg class="icon" width="40" height="40" viewBox="0 0 40 40"><circle cx="29" cy="5" r="4" fill="var(--blue)"/><path d="M12 14 L22 10 L28 18 L35 20 M22 10 L17 24 L24 30 L22 39 M17 24 L10 30 L2 30" fill="none" stroke="var(--blue)" stroke-width="4" stroke-linecap="round" stroke-linejoin="round"/></svg>
    <div class="label" style="top:74px">FREE<br>DELIVERY</div>
  </div>
  <div class="service" style="left:498px">
    <svg class="tile" width="112" height="112"><polygon points="33,0 79,0 112,33 112,79 79,112 33,112 0,79 0,33" fill="var(--tile)"/></svg>
    <svg class="icon" width="40" height="40" viewBox="0 0 40 40"><circle cx="20" cy="14" r="8" fill="none" stroke="var(--blue)" stroke-width="6" stroke-dasharray="4 2.3"/><circle cx="20" cy="14" r="5" fill="var(--blue)"/><circle cx="20" cy="14" r="2" fill="var(--tile)"/><path d="M4 26 L4 35 L36 35 L36 26" fill="none" stroke="var(--blue)" stroke-width="3"/></svg>
    <div class="label" style="top:79px">INSTALLATION</div>
  </div>
  <div class="service" style="left:622px">
    <svg class="tile" width="112" height="112"><polygon points="33,0 79,0 112,33 112,79 79,112 33,112 0,79 0,33" fill="var(--tile)"/></svg>
    <svg class="icon" width="40" height="40" viewBox="0 0 40 40"><circle cx="20" cy="5" r="4" fill="var(--blue)"/><path d="M3 8 L13 16 L27 16 L37 8" fill="none" stroke="var(--blue)" stroke-width="3.5" stroke-linecap="round"/><rect x="14" y="14" width="12" height="12" fill="var(--blue)"/><rect x="14" y="26" width="5" height="12" fill="var(--blue)"/><rect x="21" y="26" width="5" height="12" fill="var(--blue)"/></svg>
    <div class="label" style="top:79px">TRANING</div>
  </div>
  <div class="service" style="left:745px">
    <svg class="tile" width="112" height="112"><polygon points="33,0 79,0 112,33 112,79 79,112 33,112 0,79 0,33" fill="var(--tile)"/></svg>
    <svg class="icon" width="40" height="40" viewBox="0 0 40 40"><path d="M17 2 L23 2 M20 2 L20 10 M10 10 L30 10 L37 20 L3 20 Z M3 20 L37 20 L37 24 L3 24 Z" fill="none" stroke="var(--blue)" stroke-width="3"/><path d="M13 29 L12 33 M18 29 L17 33 M23 29 L22 33 M28 29 L27 33" stroke="var(--blue)" stroke-width="1.5"/></svg>
    <div class="label" style="top:74px">DRAIN AND<br>FILLS</div>
  </div>
</div>

<h2 class="section-title heading products-title abs">OUR PRODUCTS</h2>
<div class="product" style="left:171px">
  <div class="photo" role="img" aria-label="White corner bathtub with a beige tiled surround under a window" style="background:linear-gradient(160deg,#e8e2d6,#c9b79c 60%,#7a5a3e)"></div>
  <p>Lorem ipsum dolor sit amet,<br>consectetuer adipiscing elit,</p>
  <a class="btn" href="#">VIEW MORE</a>
</div>
<div class="product" style="left:388px">
  <div class="photo" role="img" aria-label="Outdoor hot tub with light blue water set against a stone wall" style="background:linear-gradient(180deg,#4d4a47 0,#6a625b 25%,#9fdbe8 45%,#c8eef4 75%,#c86a3a 100%)"></div>
  <p>Lorem ipsum dolor sit amet,<br>consectetuer adipiscing elit,</p>
  <a class="btn" href="#">VIEW MORE</a>
</div>
<div class="product" style="left:604px">
  <div class="photo" role="img" aria-label="White corner whirlpool tub with a wooden headrest" style="background:linear-gradient(170deg,#a96a4c 0,#e9e5e0 30%,#f6f4f1 70%,#a5623f 100%)"></div>
  <p>Lorem ipsum dolor sit amet,<br>consectetuer adipiscing elit,</p>
  <a class="btn" href="#">VIEW MORE</a>
</div>
<div class="product" style="left:821px">
  <div class="photo" role="img" aria-label="Indoor corner spa tub in a bright room with a window" style="background:linear-gradient(160deg,#f1ebe1,#d9c7ad 55%,#9e7556)"></div>
  <p>Lorem ipsum dolor sit amet,<br>consectetuer adipiscing elit,</p>
  <a class="btn" href="#">VIEW MORE</a>
</div>

<footer class="site-footer abs"></footer>
<div class="foot-col abs" style="left:171px">
  <h3>NEWS LETTER</h3>
  <p>Lorem ipsum dolor sit amet,<br>consectetuer adipiscing elit,</p>
</div>
<div class="newsletter-form abs"><div class="field"></div><a class="btn send" href="#">SEND NOW</a></div>
<div class="foot-col accessories abs" style="left:572px">
  <h3 style="margin-bottom:2px">ACCESSORIES</h3>
  <ul>
    <li>Lorem ipsum dolor sit amet,</li>
    <li>Consectetuer adipiscing elit,</li>
    <li style="border-bottom:none">Adipiscing elit,consectetuer</li>
  </ul>
</div>
<div class="foot-col contact abs" style="left:883px">
  <h3>CONTACT US</h3>
  <p><b>0845 000 4821</b><br>INFO@SPASHOPMAIL.EXAMPLE<br>2ND FLOOR, 88-90 ST<br>LARCH STREET,<br>LONDON, EC2X 9QT</p>
</div>
<div class="copyright abs">© 2001-2013 SPA SHOP ALBUQUERQUE</div>

</body>
</html>
```